Design a 1-page brochure with our "The Harborline Pathway" illustrated.

i have included my logo, an outline of the text and name of each step, and a quick sketch of generally how i would like the image to look. But please make it look sexy.

Each step should include the subtext as shown on the pdf attached. i.e. The first part of the image (far left) is "Problems", under that should list : 1. Poor Expectations; 2. Poor Communication... and so on for all the steps included.

I have also included a previous brochure that shows our branding and style.

Target Market(s)

Restaurant, Retail, Commercial

Industry/Entity Type

Construction Management

Font styles to use
Sans Serif

Colors
EB3D1F
EC4F4E
F09395
F8D3D4
FCEDEE

Requirements
Must have
• Our logo. Title of graphic: The Harborline Pathway, our website and IG. www.brevanbuildco.example. @brevanbuildco

```html
<!DOCTYPE html>
<html lang="en">
<head>
<meta charset="utf-8">
<title>The Harborline Pathway</title>
<link href="https://fonts.googleapis.com/css2?family=Archivo:wght@800&family=Montserrat:wght@700;800&family=Questrial&display=swap" rel="stylesheet">
<style>
  :root{
    --paper:#e6e7e8;
    --brand-red:#e3312a;
    --ink:#111111;
    --body:#3a3a3a;
    --white:#ffffff;
    --blue-a:#1dbbe5; --blue-b:#2b8cd3; --blue-t:#2283cc;
    --amber-a:#fbb23b; --amber-b:#f7853a; --amber-t:#f47a2a;
    --violet-a:#7262b0; --violet-b:#5c429c; --violet-t:#5a43a0;
    --green-a:#66bd47; --green-b:#20964a; --green-t:#1f9a49;
    --flame-a:#f7931e; --flame-b:#f0562a; --flame-t:#ee4f25;
    --teal-a:#1ba78e; --teal-b:#0d745c; --teal-t:#0f7d62;
  }
  *{margin:0;padding:0;box-sizing:border-box}
  html,body{width:1200px;height:882px;overflow:hidden;background:var(--paper)}
  .brochure{position:relative;width:1200px;height:882px;background:var(--paper);font-family:"Questrial",sans-serif}
  .frame{position:absolute;left:32px;top:24px;width:1136px;height:834px;border:1.5px solid var(--brand-red)}
  .title{position:absolute;left:0;right:0;top:154px;text-align:center;font-family:"Archivo",sans-serif;font-weight:800;font-size:54px;letter-spacing:1px;color:var(--brand-red);text-shadow:0 6px 10px rgba(0,0,0,.12)}
  .title-shadow{position:absolute;left:265px;width:670px;top:234px;height:10px;border-radius:50%;background:radial-gradient(ellipse at center,rgba(0,0,0,.08),rgba(0,0,0,0) 70%)}

  .step{position:absolute;width:139px;height:230px}
  .step.high{top:307px}
  .step.low{top:367px}
  .step .ground{position:absolute;left:-20px;width:180px;top:205px;height:26px;border-radius:50%;background:radial-gradient(ellipse at center,rgba(0,0,0,.12),rgba(0,0,0,0) 70%)}
  .step .block{position:absolute;left:0;top:0;width:139px;height:176px;border-radius:20px;box-shadow:0 8px 14px rgba(0,0,0,.12)}
  .step .num{position:absolute;left:0;right:0;top:10px;text-align:center;font-size:40px;color:var(--white);line-height:1}
  .step .panel{position:absolute;left:15px;top:76px;width:109px;height:124px;background:var(--white);border-radius:9px;padding:9px 9px 0 10px;box-shadow:0 4px 8px rgba(0,0,0,.08)}
  .step .panel::before{content:"";position:absolute;left:44px;top:-13px;border-left:10px solid transparent;border-right:10px solid transparent;border-bottom:14px solid var(--white)}
  .step h2{font-family:"Montserrat",sans-serif;font-weight:800;font-size:10.5px;line-height:1.2;text-transform:uppercase;margin-bottom:4px}
  .step ul{list-style:none}
  .step li{font-size:5.4px;color:var(--body);line-height:1.25;margin-bottom:5.5px;padding-left:6px;position:relative}
  .step li::before{content:"✓";position:absolute;left:0;top:0}
  .step .badge{position:absolute;left:52px;top:188px;width:35px;height:35px;border-radius:50%;display:flex;align-items:center;justify-content:center;box-shadow:0 5px 8px rgba(0,0,0,.25)}
  .step .badge svg{width:21px;height:21px}

  .s1{left:110px} .s1 .block,.s1 .badge{background:linear-gradient(180deg,var(--blue-a),var(--blue-b))} .s1 h2{color:var(--blue-t)}
  .s2{left:282px} .s2 .block,.s2 .badge{background:linear-gradient(180deg,var(--amber-a),var(--amber-b))} .s2 h2{color:var(--amber-t)}
  .s3{left:451px} .s3 .block,.s3 .badge{background:linear-gradient(180deg,var(--violet-a),var(--violet-b))} .s3 h2{color:var(--violet-t)}
  .s4{left:613px} .s4 .block,.s4 .badge{background:linear-gradient(180deg,var(--green-a),var(--green-b))} .s4 h2{color:var(--green-t)}
  .s5{left:784px} .s5 .block,.s5 .badge{background:linear-gradient(180deg,var(--flame-a),var(--flame-b))} .s5 h2{color:var(--flame-t)}
  .s6{left:953px} .s6 .block,.s6 .badge{background:linear-gradient(180deg,var(--teal-a),var(--teal-b))} .s6 h2{color:var(--teal-t)}
  .s6 li{margin-bottom:4px}

  .site{position:absolute;left:84px;top:794px;font-size:22px;letter-spacing:6.2px;color:var(--ink)}
  .site .domain{color:var(--brand-red)}
  .rule{position:absolute;left:610px;width:350px;top:809px;height:1.5px;background:var(--ink)}
  .brand-mark{position:absolute;left:1022px;top:700px;width:56px;height:56px;background:var(--brand-red)}
  .brand-name{position:absolute;left:972px;width:158px;top:802px;text-align:center;font-family:"Montserrat",sans-serif;font-weight:800;font-size:12.5px;color:var(--ink)}
</style>
</head>
<body>
<main class="brochure">
  <div class="frame"></div>
  <h1 class="title">THE HARBORLINE PATHWAY</h1>
  <div class="title-shadow"></div>

  <section class="step high s1">
    <div class="ground"></div>
    <div class="block"><div class="num">01</div></div>
    <div class="panel">
      <h2>Common<br>Problems</h2>
      <ul>
        <li>Changing or poor expectations.</li>
        <li>Poor Communication</li>
        <li>No Journey To Success</li>
        <li>No Trust</li>
        <li>No Accountability</li>
      </ul>
    </div>
    <div class="badge"><svg viewBox="0 0 24 24" fill="none" stroke="#fff" stroke-width="1.6" stroke-linecap="round"><circle cx="12" cy="12" r="10"/><path d="M9 9.2a3 3 0 1 1 4.2 2.7c-.8.4-1.2 1-1.2 1.9v.6"/><circle cx="12" cy="17.4" r=".6" fill="#fff"/></svg></div>
  </section>

  <section class="step low s2">
    <div class="ground"></div>
    <div class="block"><div class="num">02</div></div>
    <div class="panel">
      <h2>Organize</h2>
      <ul>
        <li>Develop Project Plan</li>
        <li>Develop Schedule</li>
        <li>Develop Budget</li>
      </ul>
    </div>
    <div class="badge"><svg viewBox="0 0 24 24" fill="#fff"><circle cx="12" cy="6" r="2.4"/><circle cx="6" cy="8" r="2"/><circle cx="18" cy="8" r="2"/><path d="M8.5 14a3.5 3.5 0 0 1 7 0v1h-7z"/><path d="M3 15a3 3 0 0 1 5-2.2V16H3z"/><path d="M21 15a3 3 0 0 0-5-2.2V16h5z"/><circle cx="12" cy="18.5" r="2.5" fill="none" stroke="#fff" stroke-width="1.4"/></svg></div>
  </section>

  <section class="step high s3">
    <div class="ground"></div>
    <div class="block"><div class="num">03</div></div>
    <div class="panel">
      <h2>Execute</h2>
      <ul>
        <li>Project Start</li>
      </ul>
    </div>
    <div class="badge"><svg viewBox="0 0 24 24" fill="none" stroke="#fff" stroke-width="1.5" stroke-linejoin="round"><path d="M10.3 2.5h3.4l.5 2.6 1.9.8 2.2-1.5 2.4 2.4-1.5 2.2.8 1.9 2.5.5v3.4l-2.5.5-.8 1.9 1.5 2.2-2.4 2.4-2.2-1.5-1.9.8-.5 2.5h-3.4l-.5-2.5-1.9-.8-2.2 1.5-2.4-2.4 1.5-2.2-.8-1.9-2.5-.5v-3.4l2.5-.5.8-1.9-1.5-2.2 2.4-2.4 2.2 1.5 1.9-.8z"/><circle cx="12" cy="12" r="3.5"/></svg></div>
  </section>

  <section class="step low s4">
    <div class="ground"></div>
    <div class="block"><div class="num">04</div></div>
    <div class="panel">
      <h2>Manage</h2>
      <ul>
        <li>O.O.D.A</li>
        <li>Shared Consciousness Meetings</li>
        <li>Pressurized Collaboration</li>
      </ul>
    </div>
    <div class="badge"><svg viewBox="0 0 24 24" fill="#fff"><circle cx="9" cy="7" r="4"/><path d="M2 20a7 7 0 0 1 12-5v5z"/><circle cx="17.5" cy="17" r="3.2" fill="none" stroke="#fff" stroke-width="2.2" stroke-dasharray="2 1.4"/><circle cx="17.5" cy="17" r="1.1"/></svg></div>
  </section>

  <section class="step high s5">
    <div class="ground"></div>
    <div class="block"><div class="num">05</div></div>
    <div class="panel">
      <h2>Complete</h2>
      <ul>
        <li>Project Closeout</li>
      </ul>
    </div>
    <div class="badge"><svg viewBox="0 0 24 24" fill="none" stroke="#fff" stroke-width="1.8" stroke-linecap="round" stroke-linejoin="round"><path d="M20 11.5A8.5 8.5 0 1 1 15 4"/><path d="M7.5 11.5l4 4L21 5"/></svg></div>
  </section>

  <section class="step low s6">
    <div class="ground"></div>
    <div class="block"><div class="num">06</div></div>
    <div class="panel">
      <h2>Possibility</h2>
      <ul>
        <li>Project Synergy.</li>
        <li>Excellent Communication where Budget and Schedule are visible and approved.</li>
        <li>Clear project visibility where everyone understands how we get to a successful end.</li>
        <li>Everyone involved is proud of the final product</li>
      </ul>
    </div>
    <div class="badge"><svg viewBox="0 0 24 24" fill="none" stroke="#fff" stroke-width="1.4" stroke-linecap="round"><circle cx="12" cy="7" r="4"/><path d="M12 11v10M12 15l-4-3M12 14l4-3"/><circle cx="6" cy="18" r="2"/><circle cx="18" cy="18" r="2"/></svg></div>
  </section>

  <p class="site">www.<span class="domain">brevanbuildco</span>.example</p>
  <div class="rule"></div>
  <div class="brand-mark"></div>
  <p class="brand-name">BREVAN BUILD CO</p>
</main>
</body>
</html>
```